Quendra - Clear Spirit Cosmetics

Please design a logo and business cards for new food supplements, cosmetics and herbal fixatives. The products are produced ecologically and biologically in the South Tyrol and Trentino alps. The products are pure and noble. Quendra = pure vitality Colors Background: dark or black matt (soft touch) Logodesign: powerful, elegant, violet with glossy foil The logo and design should convey warmth, passion and the 6th sense, you should get the impression that you can smell the herbal odor , Logo and business cards for new food supplements, cosmetics and herbal fixatives. The products are produced ecologically and biologically in the South Tyrol and Trentino alps. The products are pure and noble. Quendra = pure vitality Colors Background: dark or black matt (softtouch) Logodesign: powerful elegant violet with glossy foil The logo and design is meant to convey warmth, passion and the 6th sense, you should get the impression that you can smell the herbal perfume.

Target Market(s)

Food, food supplements, vitality, health

Contact Information for Business Card

Please provide an elegant darf design that is puristic, but has a very good logo design
Elegantes dunkles design, puristisch

Logo Text

Quendra - clear Spirit

Colors
6b449b

Requirements
Must have
• SVG Files Alpha channel for foil embossing High-quality design
Nice to have
• Pure elegance
Should not have
• to colorful colors

```html
<!DOCTYPE html>
<html lang="en">
<head>
<meta charset="utf-8">
<title>Quendra – Business Card</title>
<link rel="stylesheet" href="https://fonts.googleapis.com/css2?family=Cinzel:wght@400;700&family=Source+Sans+3:wght@400;600&display=swap">
<style>
  :root {
    --stage: #323232;
    --card-matte: #18161b;
    --brand-violet: #6b449b;
    --violet-soft: #a386cc;
    --wordmark-silver: #c9c4cf;
    --text-light: #d8d4dc;
    --white: #ffffff;
  }
  html, body {
    margin: 0;
    padding: 0;
    width: 1200px;
    height: 900px;
    overflow: hidden;
    background: var(--stage);
  }
  .stage {
    position: relative;
    width: 1200px;
    height: 900px;
    background: var(--stage);
  }
  .card {
    position: absolute;
    top: 170px;
    width: 347px;
    height: 561px;
    text-align: center;
  }
  .card--front { left: 259px; background: var(--card-matte); }
  .card--back { left: 631px; background: var(--brand-violet); }

  .brand-dot {
    position: absolute;
    left: 50%;
    width: 34px;
    height: 34px;
    border-radius: 50%;
    transform: translateX(-50%);
  }
  .card--front .brand-dot { top: 126px; background: var(--brand-violet); }
  .card--back .brand-dot { top: 238px; background: var(--white); }

  .wordmark {
    position: absolute;
    left: 0;
    right: 0;
    margin: 0;
    font-family: "Cinzel", serif;
    font-weight: 400;
    font-size: 44px;
    letter-spacing: 5px;
    line-height: 1;
  }
  .card--front .wordmark { top: 202px; color: var(--wordmark-silver); }
  .card--back .wordmark { top: 312px; color: var(--white); }

  .holder {
    position: absolute;
    left: 0;
    right: 0;
    top: 340px;
    font-family: "Source Sans 3", sans-serif;
    color: var(--text-light);
    font-size: 15px;
  }
  .holder-name {
    margin: 0;
    font-family: "Cinzel", serif;
    font-weight: 700;
    font-size: 19px;
    letter-spacing: 0.5px;
    color: var(--violet-soft);
    line-height: 24px;
  }
  .holder-role { margin: 0 0 18px; line-height: 22px; }
  .contact-list { list-style: none; margin: 0; padding: 0; line-height: 21px; }
  .contact-label { color: var(--violet-soft); font-weight: 600; }
  .contact-web { color: var(--violet-soft); font-weight: 600; }
  .address { margin: 14px 0 0; line-height: 17px; }
</style>
</head>
<body>
<main class="stage">
  <section class="card card--front">
    <span class="brand-dot"></span>
    <h1 class="wordmark">QUENDRA</h1>
    <div class="holder">
      <h2 class="holder-name">LORENZ AICHNER</h2>
      <p class="holder-role">Managing Director</p>
      <ul class="contact-list">
        <li><span class="contact-label">P:</span> 823-555-0147</li>
        <li><span class="contact-label">E:</span> hello@quendra-mail.com</li>
        <li class="contact-web">www.quendrashop.com</li>
      </ul>
      <p class="address">18, Via dei Larici<br>Bolzano, Italy 39100</p>
    </div>
  </section>

  <section class="card card--back">
    <span class="brand-dot"></span>
    <p class="wordmark">QUENDRA</p>
  </section>
</main>
</body>
</html>
```